KV HOLDWELL GROUP LETTERHEAD

I need letterhead for "KV Holdwell group LLC" ...

logo attached to project...

Company Info:
845 North Marlow Avenue, Suite 7B
Chicago, Illinois 60611
ofc 312-555-0184
facsimile 312-555-0172
www.kvholdwellgroup.example
info@kvholdwellgroup.example

I have multiple projects listed.. see below:

Business cards for ashford lane equity llc
letterhead
envelopes

Business cards for KV Holdwell LLC
letterhead
envelopes

```html
<!DOCTYPE html>
<html lang="en">
<head>
<meta charset="utf-8">
<title>KV Holdwell Group LLC – Stationery</title>
<link rel="stylesheet" href="https://fonts.googleapis.com/css2?family=Crimson+Text:ital,wght@0,400;0,600;1,400&family=Roboto+Condensed:wght@400&display=swap">
<style>
  :root {
    --board: #d9d9d9;
    --paper: #ffffff;
    --navy: #1f3564;
    --card-blue: #16457a;
    --brand-blue: #1a4a85;
    --ink: #3a3a3a;
    --label-blue: #9fb3d6;
    --caption: #333333;
    --shadow: 4px 5px 9px rgba(0,0,0,0.38);
  }
  * { margin: 0; padding: 0; box-sizing: border-box; }
  html, body { width: 1200px; height: 1000px; overflow: hidden; }
  body {
    background: var(--board);
    position: relative;
    font-family: "Crimson Text", "Times New Roman", serif;
  }
  .brand-name {
    font-variant: small-caps;
    font-weight: 400;
    letter-spacing: 0.5px;
    white-space: nowrap;
  }
  .center { position: absolute; left: 0; right: 0; text-align: center; }

  /* Letterhead */
  .letterhead {
    position: absolute; left: 120px; top: 24px;
    width: 729px; height: 944px;
    background: var(--paper);
    box-shadow: var(--shadow);
  }
  .letterhead .brand-name { top: 106px; font-size: 22px; color: var(--brand-blue); }
  .letterhead .address { top: 143px; font-size: 14px; color: var(--ink); }
  .letterhead-footer {
    position: absolute; left: 0; bottom: 0;
    width: 100%; height: 101px;
    background: var(--navy);
    color: var(--paper);
  }
  .letterhead-footer .contact { top: 31px; font-size: 14px; }
  .letterhead-footer .web { top: 52px; font-size: 17px; letter-spacing: 0.3px; }
  .label { color: var(--label-blue); }
  .sep { margin: 0 8px; color: var(--label-blue); }

  /* Business card front */
  .card {
    position: absolute; left: 786px;
    width: 349px;
    box-shadow: var(--shadow);
    overflow: hidden;
  }
  .card-front { top: 227px; height: 228px; background: var(--card-blue); color: var(--paper); }
  .card-front .brand-name { top: 120px; font-size: 23px; }
  .card-front .person { top: 160px; font-size: 17px; }
  .card-front .role { top: 180px; font-size: 14px; font-style: italic; color: #d6deea; }

  /* Business card back */
  .card-back { top: 473px; height: 227px; background: var(--paper); }
  .card-back .brand-name { top: 78px; font-size: 17px; color: var(--brand-blue); }
  .card-back .address { top: 101px; font-size: 11.5px; color: var(--ink); }
  .card-back .web { top: 116px; font-size: 12.5px; font-weight: 600; color: #111; }
  .card-back-band {
    position: absolute; left: 0; bottom: 0;
    width: 100%; height: 82px;
    background: var(--card-blue); color: var(--paper);
  }
  .card-back-band .contact { top: 24px; font-size: 12.5px; }
  .card-back-band .email { top: 40px; font-size: 12px; }
  .card-back-band .sep { margin: 0 5px; color: var(--paper); }

  .caption {
    position: absolute; left: 882px; top: 724px;
    font-family: "Roboto Condensed", "Arial Narrow", sans-serif;
    font-size: 42px; line-height: 56px;
    color: var(--caption);
  }
</style>
</head>
<body>

  <section class="letterhead">
    <div class="brand-name center">KV Holdwell Group LLC</div>
    <div class="address center">845 North Marlow Avenue, Suite 7B, Chicago, Illinois 60611</div>
    <footer class="letterhead-footer">
      <div class="contact center">
        <span class="label">T:</span> 312-555-0184<span class="sep">|</span><span class="label">F:</span> 312-555-0172<span class="sep">|</span><span class="label">E:</span> info@kvholdwellgroup.example
      </div>
      <div class="web center">www.kvholdwellgroup.example</div>
    </footer>
  </section>

  <section class="card card-front">
    <div class="brand-name center">KV Holdwell Group LLC</div>
    <div class="person center">Daniel R. Moreau, CPA MST</div>
    <div class="role center">Principal</div>
  </section>

  <section class="card card-back">
    <div class="brand-name center">KV Holdwell Group LLC</div>
    <div class="address center">845 North Marlow Avenue, Suite 7B, Chicago, Illinois 60611</div>
    <div class="web center">www.kvholdwellgroup.example</div>
    <div class="card-back-band">
      <div class="contact center">T: 312-555-0184<span class="sep">|</span>M: 312-555-0149<span class="sep">|</span>F: 312-555-0172</div>
      <div class="email center">E: dmoreau@kvholdwellgroup.example</div>
    </div>
  </section>

  <div class="caption">Business Card<br>Front &amp; Back</div>

</body>
</html>
```